Tolvane Air Center needs a new upscale business card design for our high end aircraft hangar complex

Tolvane Air Center (TAC) is a large, upscale jet hangar complex in the US housing expensive aircraft. We need a new business card design, using our current logo. We will be attending a industry convention and need a card design that will stand out and be remembered by aircraft owners and private pilots.

Target Market(s)

Aircraft pilots or owners looking for a new upscale hangar

Industry/Entity Type

Airport

I like to use very heavy card stock, 400#, double sided. Square, no rounded edges please.

Colors
3276b5
0255a3
85abd2

Requirements
Must have
• An expensive, classy design, vivid colors.
Nice to have
• Needs to look very expensive and classy, and have some "pop". Designer must be able to download or copy my current typeface or fonts.
• One card side might be black with the "Logo and Tolvane Air Center Double line image in blue (or try gold, or glossy black), and perhaps have a grayed out "R470 jet silhouette". The other card side would have our contact info, and perhaps the "TAC Logo only". I'd like my contact info 'stacked', not in a paragraph format.
Should not have
• Should not look "too busy". Having a double-sided card will help.

```html
<!DOCTYPE html>
<html lang="en">
<head>
<meta charset="utf-8">
<title>Tolvane Air Center – Business Card</title>
<link rel="stylesheet" href="https://fonts.googleapis.com/css2?family=Open+Sans:wght@400;600;700&display=swap">
<style>
  :root {
    --bg: #2b2724;
    --card: #0d0d0e;
    --card-edge: #1c1c1e;
    --blue: #3276b5;
    --blue-bright: #2f8fd6;
    --blue-deep: #0255a3;
    --blue-light: #85abd2;
    --white: #f2f2f2;
    --silver: #cfd2d6;
    --divider: #26272a;
  }
  * { box-sizing: border-box; margin: 0; padding: 0; }
  html, body { width: 1200px; height: 900px; overflow: hidden; }
  body {
    background: var(--bg);
    font-family: "Open Sans", sans-serif;
    display: flex;
    align-items: center;
    justify-content: center;
    gap: 40px;
  }
  .card {
    width: 540px;
    height: 309px;
    background: var(--card);
    border: 1px solid var(--card-edge);
    position: relative;
    color: var(--white);
  }

  /* Contact side */
  .card-front .brand {
    position: absolute;
    left: 36px;
    bottom: 74px;
    display: flex;
    align-items: center;
    gap: 10px;
  }
  .brand-dot {
    width: 14px; height: 14px;
    border-radius: 50%;
    background: var(--blue-bright);
  }
  .card-front .brand-name {
    font-size: 22px;
    font-weight: 700;
    color: var(--blue-bright);
    letter-spacing: 0.2px;
  }
  .card-front .divider {
    position: absolute;
    left: 270px;
    top: 28px;
    bottom: 28px;
    width: 1px;
    background: var(--divider);
  }
  .contact {
    position: absolute;
    left: 292px;
    top: 40px;
    font-size: 13px;
    line-height: 1.35;
  }
  .contact-name {
    font-size: 17px;
    font-weight: 700;
    color: var(--blue-bright);
  }
  .contact-title { margin-bottom: 14px; }
  .contact-address { margin-bottom: 14px; }
  .contact-list { list-style: none; }
  .contact-list li {
    display: flex;
    align-items: center;
    gap: 10px;
    height: 21px;
  }
  .contact-list svg { width: 11px; height: 11px; flex: none; fill: var(--blue-bright); }

  /* Logo side */
  .card-back {
    display: flex;
    align-items: center;
    justify-content: center;
  }
  .card-back .brand {
    display: flex;
    align-items: center;
    gap: 12px;
    margin-top: -20px;
  }
  .card-back .brand-dot { background: var(--silver); width: 16px; height: 16px; }
  .card-back .brand-name {
    font-size: 30px;
    font-weight: 700;
    color: var(--silver);
  }
</style>
</head>
<body>

  <section class="card card-front" aria-label="Card contact side">
    <div class="brand">
      <span class="brand-dot"></span>
      <span class="brand-name">Tolvane Air Center</span>
    </div>
    <div class="divider"></div>
    <div class="contact">
      <p class="contact-name">Marcus Ellery</p>
      <p class="contact-title">Managing Director</p>
      <p class="contact-address">12345, Address Goes Here<br>Country Name, 123456.</p>
      <ul class="contact-list">
        <li>
          <svg viewBox="0 0 12 12" aria-hidden="true"><path d="M2.5 0.5l2 2.2-1 1.3c.6 1.5 1.9 2.9 3.5 3.5l1.3-1 2.2 2-1.3 2C5 11.8.2 7 .5 1.8z"/></svg>
          <span>(044)-456-7890</span>
        </li>
        <li>
          <svg viewBox="0 0 12 12" aria-hidden="true"><path d="M3 0h6v3H3zM0 4h12v5h-2v3H2V9H0zm3 4v3h6V8z"/></svg>
          <span>123-456-7890</span>
        </li>
        <li>
          <svg viewBox="0 0 12 12" aria-hidden="true"><path d="M0 2h12v1L6 7 0 3zm0 2.2l6 4 6-4V10H0z"/></svg>
          <span>info@youremail.com</span>
        </li>
        <li>
          <svg viewBox="0 0 12 12" aria-hidden="true"><circle cx="6" cy="6" r="6"/></svg>
          <span>www.website.com</span>
        </li>
      </ul>
    </div>
  </section>

  <section class="card card-back" aria-label="Card logo side">
    <div class="brand">
      <span class="brand-dot"></span>
      <span class="brand-name">Tolvane Air Center</span>
    </div>
  </section>

</body>
</html>
```